CD Album Cover design for band's first album.

We are an Australian rock band called The Copper Loom. We are seeking designs for our first album cover. The album will be self titled 'The Copper Loom'.

Samples in the upload files are 2 songs and artworks we have used for merchandise; t-shirt and stubby holders. Please message me if you'd like to listen to more of the album for better idea references.
Updates

Greetings! We have updated the briefing notes. Most important update in the "must not have" section: Please do not use the current graphics in the sample uploads. We use these for merchandise and looking for fresh ideas. Your art should not contain the words "drifting past noon" or "harbour". Thank you for your submissions to date!

Target Market(s)

International audience. The artwork will be displayed for our online presence and streaming subscriptions.

Industry/Entity Type

Entertainment Industry

Colors

Designer to choose colors to be used in the design.

Requirements
Must have
• Your cover art must be:
• · Either 3000 x 3000 pixels (preferred) or 1400 x 1400 pixels
• · PNG, GIF, JPG, or JPEG file type
• · 72 - 300dpi (300dpi is the best)
• · Less than 25mb
• · RGB color scheme (not CMYK)
Should not have
• Please do not use the current graphics in the sample uploads. We use these for merchandise and are looking for fresh ideas.
• Your art should not contain the words "drifting past noon" or "harbour".

```html
<!DOCTYPE html>
<html lang="en">
<head>
<meta charset="utf-8">
<title>The Copper Loom – Album Cover</title>
<link rel="stylesheet" href="https://fonts.googleapis.com/css2?family=Roboto:ital,wght@1,100;1,300&display=swap">
<style>
  :root {
    --page-bg: #d2d4d1;
    --space-deep: #030206;
    --space-blue: #0b2236;
    --ring-pink: #e0407c;
    --ring-violet: #9a4fe0;
    --ring-core: #1a0620;
    --figure-tone: #8c7d8c;
    --title-ink: #f4eef4;
  }
  * { margin: 0; padding: 0; box-sizing: border-box; }
  html, body {
    width: 1200px;
    height: 850px;
    overflow: hidden;
    background: var(--page-bg);
  }
  .album-cover {
    position: absolute;
    left: 240px;
    top: 65px;
    width: 720px;
    height: 720px;
    overflow: hidden;
    background:
      radial-gradient(ellipse 60% 25% at 30% 0%, var(--space-blue), transparent 70%),
      radial-gradient(ellipse 50% 25% at 95% 5%, var(--space-blue), transparent 70%),
      var(--space-deep);
  }
  .glow-orb {
    position: absolute;
    left: 0;
    top: 0;
    width: 720px;
    height: 720px;
  }
  .performer-photo {
    position: absolute;
    left: 279px;
    top: 157px;
    width: 173px;
    height: 384px;
    border-radius: 40% 40% 12% 12% / 14% 14% 6% 6%;
    background: linear-gradient(180deg, #a89aa8 0%, var(--figure-tone) 45%, #4a3a4c 100%);
    opacity: 0.85;
  }
  .album-title {
    position: absolute;
    left: 36px;
    top: 640px;
    font-family: "Roboto", sans-serif;
    font-style: italic;
    font-weight: 100;
    font-size: 63px;
    letter-spacing: -0.5px;
    color: var(--title-ink);
    white-space: nowrap;
  }
</style>
</head>
<body>
  <main class="album-cover">
    <svg class="glow-orb" viewBox="0 0 720 720" aria-hidden="true">
      <defs>
        <radialGradient id="orbFill" cx="360" cy="338" r="250" gradientUnits="userSpaceOnUse">
          <stop offset="0" stop-color="#0a0210"/>
          <stop offset="0.55" stop-color="var(--ring-core)"/>
          <stop offset="0.8" stop-color="#6a1e6a"/>
          <stop offset="0.93" stop-color="var(--ring-pink)"/>
          <stop offset="1" stop-color="var(--ring-pink)" stop-opacity="0"/>
        </radialGradient>
        <linearGradient id="ringStroke" x1="0" y1="0" x2="0" y2="1">
          <stop offset="0" stop-color="var(--ring-violet)"/>
          <stop offset="1" stop-color="var(--ring-pink)"/>
        </linearGradient>
        <radialGradient id="outerGlow" cx="360" cy="338" r="300" gradientUnits="userSpaceOnUse">
          <stop offset="0.75" stop-color="var(--ring-pink)" stop-opacity="0.35"/>
          <stop offset="1" stop-color="var(--ring-pink)" stop-opacity="0"/>
        </radialGradient>
      </defs>
      <circle class="orb-halo" cx="360" cy="338" r="300" fill="url(#outerGlow)"/>
      <circle class="orb-body" cx="360" cy="338" r="250" fill="url(#orbFill)"/>
      <circle class="orb-rim" cx="360" cy="338" r="212" fill="none" stroke="url(#ringStroke)" stroke-width="3" opacity="0.8"/>
      <circle class="orb-rim-soft" cx="360" cy="338" r="230" fill="none" stroke="url(#ringStroke)" stroke-width="14" opacity="0.35"/>
    </svg>
    <div class="performer-photo" role="img" aria-label="Photograph of a guitarist walking away, seen from behind, holding an electric guitar"></div>
    <h1 class="album-title">The Copper Loom</h1>
  </main>
</body>
</html>
```